New site design for software company, replacing current 8 year old site

The site has been up and running since 1994 getting a do-over every so often. It hasn't been updated visually since 2007.
I need a simple, clean design - The actual site content will not really change. But the dark color has to change (no more black :-)
The site is http://quorblank.com/ A software company publishing DLL-based, ActiveX and .NET controls for Windows.
While I like the carousel that is currently used (see ttp://quorblank.com/) I need new backgrounds, and overall layout, color scheme, etc.
There are just 3 basic page layouts which need to be replaced. One with the carousel header (http://quorblank.com), one with a small header (http://www.quorblank.com/Products.aspx) and one with a small header, but using the full page width (this type is not publicly accessible). The basic idea of a right pane (or left) with navigation shouldn't really be changed much, but page widths, etc. can be changed freely. (And the colors, please).
I need just html/css with the visuals (no integration, no backend, no ecommerce)

Target Market(s)

Software developers

Industry/Entity Type

Computer Software

Coding

Coded - Design and coding required

Number of Pages Required

3 page

Font styles to use
Sans Serif

Requirements
Must have
• 3 basic page layouts. One with the carousel header (http://quorblank.com), one with a small header (http://www.quorblank.com/Products.aspx) and one with a small header, but using the full page width (this type is not publicly accessible).
• NOTE: This is just for basic html/css - No other work (no integration, no backend, no ecommerce)

```html
<!DOCTYPE html>
<html lang="en">
<head>
<meta charset="utf-8">
<title>Quorblank – Software Controls</title>
<link href="https://fonts.googleapis.com/css2?family=Open+Sans:wght@400;600;700&display=swap" rel="stylesheet">
<style>
:root{
  --blue:#2b8fd6;
  --blue-dark:#1f6fae;
  --teal:#2ea6a6;
  --teal-band:#3aa6b0;
  --navy:#24486e;
  --red:#e0493e;
  --ink:#333a42;
  --muted:#7c8690;
  --line:#e3e7eb;
  --pale:#f3f6f8;
  --footer:#2d3238;
  --white:#fff;
}
*{box-sizing:border-box;margin:0;padding:0}
html,body{width:1200px;height:2960px;overflow:hidden}
body{font-family:"Open Sans",Arial,sans-serif;color:var(--ink);background:var(--white);font-size:12px;line-height:1.5}
.wrap{width:960px;margin:0 auto;position:relative}
/* header */
.topbar{height:44px;background:var(--white);border-bottom:1px solid var(--line)}
.topbar .wrap{display:flex;align-items:center;justify-content:space-between;height:44px}
.brand{display:flex;align-items:center;gap:10px}
.brand-sq{width:32px;height:32px;background:var(--blue)}
.brand-name{font-weight:700;font-size:15px;color:var(--ink)}
.brand-tag{font-size:10px;color:var(--muted);margin-left:6px}
.tools{display:flex;gap:10px;align-items:center}
.search{width:160px;height:22px;border:1px solid var(--line);font-size:10px;color:var(--muted);padding:3px 8px}
.tools a{font-size:10px;color:var(--blue);text-decoration:none}
.nav{background:var(--blue);height:30px}
.nav ul{list-style:none;display:flex;height:30px;align-items:center;gap:26px}
.nav a{color:var(--white);text-decoration:none;font-size:11px;font-weight:600}
/* hero */
.hero{background:var(--pale);height:400px;position:relative}
.hero .wrap{height:400px}
.hero-title{position:absolute;left:0;top:60px;width:260px;font-size:26px;font-weight:700;line-height:1.2}
.hero-art{position:absolute;left:280px;top:30px;width:380px;height:300px;background:linear-gradient(160deg,#e6eef5,#b9cde0)}
.hero-panel{position:absolute;right:0;top:30px;width:270px;height:300px;background:var(--blue);color:var(--white);padding:24px}
.hero-panel h2{font-size:18px;line-height:1.25;margin-bottom:12px}
.hero-panel p{font-size:11px;opacity:.9}
.hero-caption{position:absolute;left:0;right:0;bottom:24px;height:36px;background:rgba(36,72,110,.85);color:var(--white);font-size:11px;padding:10px 16px}
/* section heads */
.sec{padding-top:30px}
.sec-head{display:flex;align-items:center;gap:14px;margin-bottom:20px}
.sec-letter{width:40px;height:40px;background:var(--blue);color:var(--white);font-weight:700;font-size:18px;display:flex;align-items:center;justify-content:center}
.sec-head h2{font-size:18px;font-weight:600}
.sec-head p{font-size:10px;color:var(--muted)}
/* updates */
.updates{background:var(--white)}
.cards{display:grid;grid-template-columns:repeat(4,1fr);gap:16px}
.card{border:1px solid var(--line)}
.card-top{height:140px;color:var(--white);display:flex;flex-direction:column;align-items:center;justify-content:center}
.card-top span{font-size:12px;font-weight:600}
.card-top b{font-size:54px;font-weight:700;line-height:1}
.c1{background:var(--teal)}.c2{background:var(--blue)}.c3{background:var(--navy)}.c4{background:var(--red)}
.card-date{padding:12px 14px;font-size:15px;font-weight:600}
.card-date small{display:block;font-size:10px;color:var(--muted);font-weight:400}
/* products */
.tiles{display:grid;grid-template-columns:repeat(3,1fr);gap:20px}
.tile-logo{height:90px;border:1px solid var(--line);display:flex;align-items:center;justify-content:center;font-size:20px;font-weight:600;color:var(--navy)}
.tile-label{background:var(--blue);color:var(--white);font-size:11px;padding:6px 12px;font-weight:600}
/* lists */
.cat{border-top:1px solid var(--line);margin-top:30px;padding-top:20px}
.cat h3{font-size:15px;font-weight:600;margin-bottom:14px;display:flex;align-items:center;gap:8px}
.cat h3::before{content:"";width:8px;height:8px;background:var(--blue)}
.cat .intro{font-size:11px;color:var(--muted);margin-bottom:14px}
.items{display:grid;grid-template-columns:repeat(2,1fr);gap:18px}
.item{display:flex;gap:12px}
.thumb{width:70px;height:50px;flex:none;background:linear-gradient(135deg,#dfe9f2,#aac4dc)}
.item h4{font-size:12px;font-weight:600;color:var(--blue)}
.item p{font-size:10px;color:var(--muted)}
.vtiles{display:grid;grid-template-columns:repeat(6,1fr);gap:12px}
.vt-top{height:96px;background:var(--blue);color:var(--white);display:flex;flex-direction:column;align-items:center;justify-content:center}
.vt-top span{font-size:10px}
.vt-top b{font-size:36px;line-height:1}
.vt p{font-size:10px;color:var(--muted);margin-top:8px}
.dll{display:grid;grid-template-columns:220px 1fr;gap:30px}
/* why */
.why{background:var(--teal-band);color:var(--white);height:370px;margin-top:40px;text-align:center;padding-top:44px}
.why h2{font-size:26px;font-weight:700;margin-bottom:16px}
.why p{width:820px;margin:0 auto 10px;font-size:11px;opacity:.92}
.badges{display:flex;justify-content:center;gap:22px;margin-top:30px}
.badge{width:70px;height:70px;background:var(--white);border-radius:6px}
/* footer lists */
.flinks{display:grid;grid-template-columns:repeat(3,1fr);gap:30px;padding:40px 0 30px}
.fcol h3{display:flex;align-items:center;gap:12px;font-size:14px;font-weight:600;margin-bottom:12px}
.fcol h3 i{width:34px;height:34px;background:var(--blue);color:var(--white);font-style:normal;display:flex;align-items:center;justify-content:center;font-size:15px}
.fcol ul{list-style:none;padding-left:46px;margin-bottom:22px}
.fcol li{font-size:10px;color:var(--muted);line-height:1.9}
.footer{background:var(--footer);height:70px;color:#c5ccd3}
.footer .wrap{display:flex;align-items:center;justify-content:space-between;height:70px}
.footer ul{list-style:none;display:flex;gap:20px;font-size:11px}
.bottom{background:#22262b;height:36px;color:#8a939c;font-size:10px}
.bottom .wrap{display:flex;align-items:center;justify-content:space-between;height:36px}
</style>
</head>
<body>
<header>
  <div class="topbar"><div class="wrap">
    <div class="brand"><div class="brand-sq"></div><span class="brand-name">Quorblank</span><span class="brand-tag">Software controls since 1994</span></div>
    <div class="tools"><div class="search">Search site…</div><a href="#">Login</a><a href="#">Register</a></div>
  </div></div>
  <nav class="nav"><div class="wrap"><ul>
    <li><a href="#">Home</a></li><li><a href="#">Products</a></li><li><a href="#">Support</a></li><li><a href="#">My Account</a></li><li><a href="#">Purchase</a></li><li><a href="#">About</a></li>
  </ul></div></nav>
</header>

<section class="hero"><div class="wrap">
  <h1 class="hero-title">.NET Controls, ActiveX Controls and DLL-Based Custom Controls</h1>
  <div class="hero-art" role="img" aria-label="Product box illustration of the control suites"></div>
  <div class="hero-panel">
    <h2>.NET Controls, ActiveX Controls and DLL-Based Custom Controls</h2>
    <p>Quality controls for developers building desktop applications. Trees, tabs, print previews and more, used in thousands of projects worldwide since 1994. Each product ships with samples, full source options and direct support from the people who wrote it.</p>
  </div>
  <div class="hero-caption">.NET Controls, ActiveX Controls and DLL-Based Custom Controls</div>
</div></section>

<section class="sec updates"><div class="wrap">
  <div class="sec-head"><div class="sec-letter">U</div><div><h2>New Products &amp; Updates</h2><p>The latest releases of our control suites</p></div></div>
  <div class="cards">
    <div class="card"><div class="card-top c1"><span>QbBox/OCX</span><b>3.0</b></div><div class="card-date">August 24, 2015<small>New release available</small></div></div>
    <div class="card"><div class="card-top c2"><span>QbTabs/OCX</span><b>5.0</b></div><div class="card-date">August 24, 2015<small>New release available</small></div></div>
    <div class="card"><div class="card-top c3"><span>QbTree/NET</span><b>2.0</b></div><div class="card-date">August 24, 2015<small>New release available</small></div></div>
    <div class="card"><div class="card-top c4"><span>QbTree/OCX</span><b>7.0</b></div><div class="card-date">August 24, 2015<small>New release available</small></div></div>
  </div>
</div></section>

<section class="sec"><div class="wrap">
  <div class="sec-head"><div class="sec-letter">P</div><div><h2>Our Products</h2><p>Find the control family that fits your development environment</p></div></div>
  <div class="tiles">
    <div><div class="tile-logo">Netframe</div><div class="tile-label">.NET Controls</div></div>
    <div><div class="tile-logo">CodeStudio</div><div class="tile-label">ActiveX Controls</div></div>
    <div><div class="tile-logo">CodeStudio</div><div class="tile-label">DLL Controls</div></div>
  </div>

  <div class="cat">
    <h3>.NET Controls</h3>
    <div class="items">
      <div class="item"><div class="thumb" role="img" aria-label="Tree control screenshot"></div><div><h4>QbTabs/NET 6.0</h4><p>Tab controls for forms with dozens of styles and complete designer support built in.</p></div></div>
      <div class="item"><div class="thumb" role="img" aria-label="Tree control screenshot"></div><div><h4>QbTree/NET 2.0</h4><p>Tree control with columns, cell editing, images and fast loading of very large data sets.</p></div></div>
    </div>
  </div>

  <div class="cat">
    <h3>ActiveX Controls</h3>
    <p class="intro">Most of our ActiveX controls fully support 32-bit and 64-bit development in all popular environments, including current and older tool versions, and are used by developers who need reliable, proven components.</p>
    <div class="vtiles">
      <div class="vt"><div class="vt-top"><span>QbBox/OCX</span><b>5.0</b></div><p>Combo box control with multiple columns and images.</p></div>
      <div class="vt"><div class="vt-top"><span>QbDirectory</span><b>3.0</b></div><p>File and folder browsing in a single control.</p></div>
      <div class="vt"><div class="vt-top"><span>QbMask/OCX</span><b>3.0</b></div><p>Masked edit input with formats and validation.</p></div>
      <div class="vt"><div class="vt-top"><span>QbOptions</span><b>1.0</b></div><p>Store and manage user options with ease.</p></div>
      <div class="vt"><div class="vt-top"><span>QbTabs/OCX</span><b>7.0</b></div><p>Tab controls in many styles and layouts.</p></div>
      <div class="vt"><div class="vt-top"><span>QbTree/OCX</span><b>1.0</b></div><p>Tree control with columns and cell editing.</p></div>
    </div>
  </div>

  <div class="cat">
    <h3>DLL Controls</h3>
    <div class="dll">
      <p class="intro">Our DLL-based controls are designed for C and C++ applications using the native API directly, with small footprint and full source code options.</p>
      <div class="items">
        <div class="item"><div class="thumb" role="img" aria-label="Print preview control screenshot"></div><div><h4>QbPrintPreview/DLL 2.0</h4><p>Print preview for any application with zoom and page navigation.</p></div></div>
        <div class="item"><div class="thumb" role="img" aria-label="Tabs control screenshot"></div><div><h4>QbTabs/DLL 7.0</h4><p>Tab controls for native code with many visual styles.</p></div></div>
        <div class="item"><div class="thumb" role="img" aria-label="Tree control screenshot"></div><div><h4>QbTree/DLL 8.0</h4><p>Tree control with columns for native applications.</p></div></div>
      </div>
    </div>
  </div>
</div></section>

<section class="why">
  <h2>Why Choose Us?</h2>
  <p>We develop controls designed to make life easier for developers. Every product is built and maintained by the same small team, with a focus on quality, stability and long term compatibility across tool versions.</p>
  <p>Our customers range from single developers to large enterprises, and many have used our products for more than twenty years in mission-critical applications.</p>
  <p>Every purchase includes samples, documentation and direct support from engineers who know the code.</p>
  <div class="badges"><div class="badge"></div><div class="badge"></div><div class="badge"></div><div class="badge"></div></div>
</section>

<section><div class="wrap flinks">
  <div class="fcol">
    <h3><i>N</i>.NET Controls</h3>
    <ul><li>QbTabs/NET 6.0</li><li>QbTree/NET 2.0</li></ul>
    <h3><i>D</i>DLL Controls</h3>
    <ul><li>QbPrintPreview/DLL 2.0</li><li>QbTabs/DLL 7.0</li><li>QbTree/DLL 8.0</li></ul>
  </div>
  <div class="fcol">
    <h3><i>A</i>ActiveX Controls</h3>
    <ul><li>QbBox/OCX 5.0</li><li>QbDirectory 3.0</li><li>QbMask/OCX 3.0</li><li>QbOptions 1.0</li><li>QbTabs/OCX 7.0</li><li>QbTree/OCX 7.0</li><li>Licensing</li></ul>
  </div>
  <div class="fcol">
    <h3><i>C</i>Customer Info</h3>
    <ul><li>My Account Login Required</li><li>License Keys Login Required</li><li>Download Products</li><li>About Ordering</li><li>Frequently Asked Questions</li><li>Privacy</li></ul>
  </div>
</div></section>

<footer>
  <div class="footer"><div class="wrap">
    <div class="brand"><div class="brand-sq"></div><span class="brand-name" style="color:#fff">Quorblank</span></div>
    <ul><li>Home</li><li>Products</li><li>Support</li><li>My Account</li><li>Purchase</li><li>About</li></ul>
  </div></div>
  <div class="bottom"><div class="wrap"><span>Quorblank Inc. © 2015 &nbsp;|&nbsp; Contact</span><span>Site design and development</span></div></div>
</footer>
</body>
</html>
```